Qivera Health & Wellness Business Card Design

We would like to create business cards matching with our new logo design. The card should be professional looking but still have a playful side and something that would be eye catching. We are planing to open a luxury medical spa and looking to create a design based on this new logo. We are looking for a design that shows off luxury but not be gold in color. Also, while we are a more female oriented medical center we do have men that come in for our services and it should be be too feminine.

Target Market(s)

Health & Wellness. Medical patients. Luxury spa

Industry/Entity Type

Health And Wellness

Contact Information for Business Card

It should have the logo design in the front of card and back of card should have our contact information. Our current colors are peach/ coral, teal, and gray. We are looking for a modern looking design.

Font styles to use
Script

Colors
32a6d6
e667a6
86cfc6
fece3e

Requirements
Must have
• It should have our logo design. We would prefer to have a more modern look to the card.
Nice to have
• Eye-Catching Design on the personable side but still classy.
Should not have
• At this point we are looking for the best design. It should not have color purple.

```html
<!DOCTYPE html>
<html lang="en">
<head>
<meta charset="utf-8">
<title>Qivera Health &amp; Wellness Business Card</title>
<link href="https://fonts.googleapis.com/css2?family=Quicksand:wght@400;500&display=swap" rel="stylesheet">
<style>
  :root {
    --backdrop: #d6eeea;
    --card-white: #ffffff;
    --card-gray: #58585a;
    --pink: #e667a6;
    --teal: #5cc6b8;
    --ink: #3a3a3c;
  }
  html, body {
    margin: 0;
    padding: 0;
    width: 1200px;
    height: 1000px;
    overflow: hidden;
    background: var(--backdrop);
    font-family: "Quicksand", sans-serif;
  }
  .canvas {
    position: relative;
    width: 1200px;
    height: 1000px;
  }
  .card {
    position: absolute;
    top: 197px;
    width: 360px;
    height: 606px;
    box-shadow: 0 6px 18px rgba(0, 0, 0, 0.12);
  }
  .card--front { left: 200px; background: var(--card-white); }
  .card--back  { left: 640px; background: var(--card-gray); }

  .card__accent-line {
    position: absolute;
    left: 0;
    right: 0;
    bottom: 22px;
    height: 6px;
    background: var(--pink);
  }

  .holder {
    position: absolute;
    top: 38px;
    right: 28px;
    text-align: right;
  }
  .holder__name {
    margin: 0;
    font-size: 21px;
    font-weight: 400;
    color: var(--teal);
  }
  .holder__title {
    margin: 4px 0 0;
    font-size: 12px;
    letter-spacing: 2.5px;
    color: var(--pink);
  }

  .brand {
    position: absolute;
    left: 0;
    right: 0;
    text-align: center;
    margin: 0;
    font-size: 27px;
    font-weight: 500;
    line-height: 1.25;
    color: var(--pink);
  }
  .card--front .brand { top: 280px; }
  .card--back .brand  { top: 255px; }

  .contacts {
    position: absolute;
    left: 38px;
    bottom: 50px;
    margin: 0;
    padding: 0;
    list-style: none;
  }
  .contacts__item {
    display: flex;
    align-items: center;
    gap: 10px;
    font-size: 16px;
    color: var(--ink);
    margin-top: 7px;
  }
  .contacts__icon {
    width: 16px;
    height: 16px;
    fill: none;
    stroke: var(--pink);
    stroke-width: 1.6;
    stroke-linecap: round;
    stroke-linejoin: round;
  }

  .website {
    position: absolute;
    left: 0;
    right: 0;
    bottom: 44px;
    margin: 0;
    text-align: center;
    font-size: 13px;
    letter-spacing: 2px;
    color: var(--teal);
  }
</style>
</head>
<body>
<main class="canvas">

  <section class="card card--front" aria-label="Business card front">
    <div class="holder">
      <p class="holder__name">Here Your Name</p>
      <p class="holder__title">TITLE</p>
    </div>

    <p class="brand">Qivera<br>Health &amp; Wellness</p>

    <ul class="contacts">
      <li class="contacts__item">
        <svg class="contacts__icon" viewBox="0 0 16 16" aria-hidden="true">
          <path d="M4 2 L6 2 L7 5 L5.5 6.5 C6.5 8.5 7.5 9.5 9.5 10.5 L11 9 L14 10 L14 12 C14 13 13 14 12 14 C7 14 2 9 2 4 C2 3 3 2 4 2 Z"/>
        </svg>
        <span>0000 1111 222</span>
      </li>
      <li class="contacts__item">
        <svg class="contacts__icon" viewBox="0 0 16 16" aria-hidden="true">
          <rect x="2" y="4" width="12" height="9" rx="1"/>
          <path d="M2 5 L8 9.5 L14 5"/>
        </svg>
        <span>email@yourwebsite.com</span>
      </li>
      <li class="contacts__item">
        <svg class="contacts__icon" viewBox="0 0 16 16" aria-hidden="true">
          <path d="M8 15 C8 15 3 9.5 3 6 A5 5 0 0 1 13 6 C13 9.5 8 15 8 15 Z"/>
          <circle cx="8" cy="6" r="1.8"/>
        </svg>
        <span>123 ABC street, LG. US</span>
      </li>
    </ul>

    <div class="card__accent-line"></div>
  </section>

  <section class="card card--back" aria-label="Business card back">
    <p class="brand">Qivera<br>Health &amp; Wellness</p>
    <p class="website">www.yourwebsite.com</p>
    <div class="card__accent-line"></div>
  </section>

</main>
</body>
</html>
```